Modern home page design for insurance and investment business

- The design should be based around the attached HPID (home page information design) called KTW HPID. The table boxes are just for approximate placement of information – you DON'T have to make it look exactly like this.
- Information only is in orange text. Copy to go on the design in black text. Some instructions are in the HPID. Please be creative! You don’t have to use the exact images provided if you have a better idea.

- The design needs to be clean and spacious. Please use the colours from the logos in the website design. Lots of white too.

I've attached home page gallery example photos. You can use any of these photos or something similar with the words from one of the photos.

- Expected standard of design examples: (Please DO NOT copy these exactly – they are just examples)
http://www.harbourvane.co.nz/
https://www.brightkeel.co.nz/
http://sandorelcover.co.nz/homepage/

Width of content will be 1100 pixels when implemented as a web page. Header height (without nav bar) 150-160 pixels.

The winning PSD file will have to be provided as follows…
1. Canvas size of 2000px x 2000px - 72ppi in Adobe Photoshop (CS5 compatible)
2. Width of content section is 1100px wide - centered in the canvas
3. Any button rollovers/hovers in the PSD as hidden layers.
4. All fonts used must be Google fonts (except for the fonts in the header at the top of the page).
5. You will need to supply the chosen home page plus one example page (example page as a style guide for how all other pages will look). Example page is only the header and navigational bar at the top, an empty sector in the middle with a column (180 px wide) which can be left or right aligned which means the main sector is 920 pixels wide, and then the footer at the bottom of the page.

```html
<!DOCTYPE html>
<html lang="en">
<head>
<meta charset="utf-8">
<title>KTW Insure &amp; Invest</title>
<link href="https://fonts.googleapis.com/css2?family=Roboto+Slab:wght@400;700&family=Open+Sans:wght@400;600&family=Roboto+Condensed:wght@400&family=Arimo:ital@0;1&display=swap" rel="stylesheet">
<style>
:root{
  --blue:#0a3f7a;
  --blue-light:#1c5290;
  --grey:#9ea3a6;
  --grey-dark:#6d7276;
  --orange:#e8601c;
  --text:#333;
  --page:#f3f4f5;
  --white:#fff;
  --line:#dfe1e3;
}
*{margin:0;padding:0;box-sizing:border-box}
html,body{width:912px;height:1200px;overflow:hidden}
body{position:relative;background:var(--page);font-family:'Open Sans',sans-serif;color:var(--text)}
.abs{position:absolute}
.lower{left:0;top:376px;width:912px;height:566px;background:#fafafa}

/* header */
.brand{left:100px;top:34px;display:flex;align-items:center;gap:10px}
.brand-name{font-family:'Open Sans',sans-serif;font-weight:600;font-size:34px;color:var(--blue);letter-spacing:-1px}
.brand-mark{width:38px;height:38px;border-radius:50%;background:var(--blue)}
.map-thumb{left:346px;top:20px;width:161px;height:64px;background:linear-gradient(135deg,#c9c6bd,#b5b2a8 60%,#cfc7b0);border:1px solid #bbb}
.map-caption{left:346px;top:85px;width:166px;text-align:center;font-family:'Roboto Slab',serif;font-style:italic;font-size:9.5px;color:var(--blue)}
.tagline{left:520px;top:19px;width:284px;text-align:right;font-family:'Roboto Slab',serif;font-size:10.5px;line-height:12px;color:#555}
.call{left:589px;top:62px;display:flex;gap:6px;align-items:center}
.call-text small{display:block;font-family:Arimo,sans-serif;font-size:10.5px;color:#333}
.call-text strong{display:block;font-family:Arimo,sans-serif;font-weight:400;font-size:15px;color:#222;line-height:16px}

/* nav */
.nav{left:87px;top:101px;width:738px;height:26px;background:var(--grey);display:flex;white-space:nowrap}
.nav a{font-size:10.5px;color:var(--white);text-decoration:none;line-height:26px;padding:0 13.5px}
.nav a.active{background:var(--blue);padding:0 15px}

/* hero */
.hero{left:87px;top:142px;width:738px;height:234px;background:linear-gradient(180deg,#7a6a45 0%,#b8964f 35%,#d7b067 55%,#6a5530 78%,#111 86%,#0b0b0b 100%)}
.hero h1{position:absolute;left:14px;top:8px;font-family:'Roboto Slab',serif;font-style:italic;font-weight:400;font-size:23px;line-height:28px;color:var(--white)}
.dots{position:absolute;left:13px;bottom:12px;display:flex;gap:4px}
.dots i{width:7px;height:7px;border-radius:50%;background:#aaa}
.dots i.on{background:var(--white)}

/* feature cards */
.card{top:390px;width:356px;height:160px;background:var(--blue);color:var(--white);box-shadow:0 6px 6px -4px rgba(0,0,0,.35)}
.card h2{position:absolute;left:15px;top:8px;font-family:'Roboto Slab',serif;font-weight:400;font-size:22px}
.card p{position:absolute;left:15px;top:42px;width:228px;font-size:9.3px;line-height:12px}
.card .btn{position:absolute;left:16px;top:126px;width:88px;height:21px;background:#b3b6b8;color:#222;font-size:10px;line-height:21px;text-align:center;border-bottom:2px solid #7b7f82}
.card svg{position:absolute;left:250px;top:35px}

/* life stages */
.section-title{left:87px;top:576px;font-family:'Roboto Slab',serif;font-weight:400;font-size:17px;color:#333}
.stages{left:87px;top:605px;width:738px;height:235px;display:flex;background:var(--white);border:1px solid var(--line)}
.stage{flex:1;border-right:1px solid var(--line);position:relative}
.stage:last-child{border-right:0}
.stage h3{text-align:center;margin-top:10px;font-weight:400;font-size:12.5px;color:var(--orange)}
.stage-photo{position:absolute;left:14px;top:34px;width:156px;height:138px;border-radius:6px}
.stage ul{position:absolute;left:13px;top:176px;width:172px;list-style:none;white-space:nowrap;font-family:'Roboto Condensed',sans-serif;font-size:9.3px;line-height:14px;color:#333}

/* footer */
.footer{left:0;top:942px;width:912px;height:228px;background:var(--blue)}
.contact-band{left:472px;top:978px;width:158px;height:192px;background:var(--blue-light)}
.callback{left:87px;top:860px;width:738px;height:117px;background:var(--white);border:1px solid var(--line)}
.callback h2{position:absolute;left:15px;top:12px;font-family:'Roboto Slab',serif;font-weight:400;font-size:16px;color:#333;white-space:nowrap}
.field{position:absolute;height:26px;border:1px solid #d6d8da;background:var(--white);font-family:Arimo,sans-serif;font-style:italic;font-size:9.5px;color:#555;padding:7px 9px}
.send{position:absolute;left:668px;top:81px;width:55px;height:22px;background:#a8acae;color:#222;font-size:10.5px;text-align:center;line-height:22px}
.fcol{top:1008px;color:var(--white);font-size:9.5px;line-height:11.5px}
.fcol h4{font-family:'Roboto Slab',serif;font-weight:700;font-size:9.5px;margin-bottom:10px}
.fcol p{margin-bottom:6px}
.fmap{left:677px;top:1036px;width:135px;height:86px;background:linear-gradient(135deg,#e2e1dc,#d3d1ca)}
.bottom{left:0;top:1170px;width:912px;height:30px;background:#a6a9ab;font-family:Arimo,sans-serif;font-size:8.5px;color:#222}
.bottom .copy{position:absolute;left:103px;top:11px}
.bottom .follow{position:absolute;left:730px;top:9px;display:flex;gap:6px;align-items:center;font-size:9.5px}
.bottom .follow i{width:16px;height:16px;background:#3b5a98;display:block}
</style>
</head>
<body>
<div class="abs lower"></div>

<header>
  <div class="abs brand"><span class="brand-name">KTW</span><span class="brand-mark"></span></div>
  <div class="abs map-thumb" role="img" aria-label="Street map showing office location"></div>
  <div class="abs map-caption">Servicing clients New Zealand wide</div>
  <div class="abs tagline">Smart financial decisions for today and for your future<br>Insurances / Investments / Financial Planning</div>
  <div class="abs call">
    <svg width="22" height="22" viewBox="0 0 22 22"><circle cx="11" cy="11" r="10" fill="none" stroke="#333" stroke-width="1.4"/><path d="M8 6c-1 1-1 3 1 6s4 4 5 4l1.5-1.5-2-2-1 .8c-1-.5-2-2-2.5-3l.8-1-2-2z" fill="#333"/></svg>
    <div class="call-text"><small>Call Us Today</small><strong>0800 555 0142 | 06 555 0142</strong></div>
  </div>
</header>

<nav class="abs nav">
  <a class="active">Home</a><a>About</a><a>What We Do</a><a>What Life Stage Are You?</a><a>Insurances</a><a>Investments</a><a>FAQ’s</a><a>Consultation</a><a>Contact</a>
</nav>

<section class="abs hero" role="img" aria-label="Tractor silhouetted against a golden sunset sky over farmland">
  <h1>Lorem is the Dummy text of the indsutry<br>lorem dafew oreafdf lore dreifsad</h1>
  <div class="dots"><i></i><i></i><i></i><i class="on"></i></div>
</section>

<article class="abs card" style="left:87px">
  <h2>Insurance</h2>
  <p>An overview of insurance from the point of view of benefits to the customer of working with KTW will be in this space..... Relevant keywords such as the types of insurances e.g. life insurance, travel insurance etc will be mentioned... Should be inviting to both new and current customers.....</p>
  <svg width="92" height="92" viewBox="0 0 92 92"><circle cx="46" cy="46" r="44" fill="#a3a7aa" stroke="#fff" stroke-width="5"/><path d="M24 44a22 18 0 0 1 44 0z" fill="#222"/><rect x="45" y="22" width="2" height="6" fill="#222"/><rect x="32" y="48" width="28" height="20" fill="none" stroke="#222" stroke-width="3"/><text x="46" y="63" text-anchor="middle" font-family="Open Sans,sans-serif" font-size="13" font-weight="600" fill="#222">$</text></svg>
  <div class="btn">Find Out More</div>
</article>

<article class="abs card" style="left:469px">
  <h2>Investment</h2>
  <p>An overview of insurance from the point of view of benefits to the customer of working with KTW will be in this space..... Relevant keywords such as the types of insurances e.g. life insurance, travel insurance etc will be mentioned... Should be inviting to both new and current customers.....</p>
  <svg width="92" height="92" viewBox="0 0 92 92"><circle cx="46" cy="46" r="44" fill="#a3a7aa" stroke="#fff" stroke-width="5"/><rect x="24" y="54" width="9" height="14" fill="#222"/><rect x="37" y="48" width="9" height="20" fill="#222"/><rect x="50" y="44" width="9" height="24" fill="#222"/><rect x="63" y="38" width="9" height="30" fill="#222"/><path d="M24 46l14-12 8 6 18-16" fill="none" stroke="#222" stroke-width="3"/><path d="M58 20h10v10z" fill="#222"/></svg>
  <div class="btn">Find Out More</div>
</article>

<h2 class="abs section-title">What life stage are you at?</h2>
<section class="abs stages">
  <div class="stage"><h3>18-30 years</h3>
    <div class="stage-photo" style="background:linear-gradient(180deg,#c9d8e6,#e6c7b0)" role="img" aria-label="Photo of a young couple in a thought-bubble frame"></div>
    <ul><li>Should I start financial planning now?</li><li>What insurances do we need?</li><li>What is the best way to save?</li></ul></div>
  <div class="stage"><h3>30-45 years</h3>
    <div class="stage-photo" style="background:linear-gradient(180deg,#a9c9e6,#dfbd9c)" role="img" aria-label="Photo of a young family in a thought-bubble frame"></div>
    <ul><li>How do we create a balanced financial plan?</li><li>Have we got the right insurance cover?</li><li>Which investments are best for us?</li></ul></div>
  <div class="stage"><h3>45-65 years</h3>
    <div class="stage-photo" style="background:linear-gradient(180deg,#8fb6de,#4f82b8)" role="img" aria-label="Photo of a middle-aged couple by the sea in a thought-bubble frame"></div>
    <ul><li>Are we on track for retirement savings?</li><li>Is our health insurance cover enough?</li><li>Have we correctly structured our business?</li></ul></div>
  <div class="stage"><h3>65+ years</h3>
    <div class="stage-photo" style="background:linear-gradient(180deg,#bcd3a4,#eadcba)" role="img" aria-label="Photo of a retired couple in a thought-bubble frame"></div>
    <ul><li>Can we take our dream holiday?</li><li>Should we consider downsizing the house?</li><li>How often should we revise our will?</li></ul></div>
</section>

<footer>
  <div class="abs footer"></div>
  <div class="abs contact-band"></div>
  <div class="abs fcol" style="left:103px"><h4>Quick Links</h4><p style="padding-left:4px">Home</p><p style="padding-left:4px;margin-bottom:6px">About<br>• Meet the Team<br>• Testimonials</p><p style="padding-left:4px">What We Do</p><p style="padding-left:4px">FAQ’s</p><p style="padding-left:4px">Consultation</p></div>
  <div class="abs fcol" style="left:206px"><h4>What Life Stage are You?</h4><p style="line-height:15.5px">• Life stage 18-30 years<br>• Life stage 30-45 years<br>• Life stage 45-65 years<br>• Life stage 65+ years</p></div>
  <div class="abs fcol" style="left:355px"><h4>Products/Services</h4><p style="margin-top:-4px">Insurances<br>• Life insurance<br>• Trauma insurance<br>• Disablement cover<br>• Income protection<br>• Health insurance<br>• Business insurance<br>• Fire &amp; General<br>• Travel insurance</p><p>Investment<br>• NestSaver</p></div>
  <div class="abs fcol" style="left:484px"><h4>Contact Details</h4><p>48 Tidewell Rd., Harbourton<br>New Zealand<br>PO Box 5402, Harbourton</p><p style="margin-top:10px">Office Hours: 8.30am – 5.00pm</p><p style="margin-top:10px">After Hours: Please Phone:<br>0800 555 0142 | 06 555 0142</p></div>
  <div class="abs fcol" style="left:677px"><h4 style="font-weight:400">Location Map</h4></div>
  <div class="abs fmap" role="img" aria-label="Street map of office location"></div>
  <div class="abs fcol" style="left:679px;top:1130px;font-size:8.5px">View Location &gt;&gt;</div>

  <form class="abs callback">
    <h2>Would you like KTW to call you? Fill in the form and we’ll be in touch...</h2>
    <div class="field" style="left:13px;top:44px;width:166px">First Name</div>
    <div class="field" style="left:184px;top:44px;width:166px">Email</div>
    <div class="field" style="left:13px;top:76px;width:166px">Last Name</div>
    <div class="field" style="left:184px;top:76px;width:166px">Phone Number</div>
    <div class="field" style="left:356px;top:44px;width:304px;height:60px">Message</div>
    <div class="send">Send</div>
  </form>

  <div class="abs bottom"><span class="copy">Copyright ©2014, KTW Insure &amp; Invest.  All Rights Reserved</span><span class="follow">Follow Us On <i></i></span></div>
</footer>
</body>
</html>
```